Lone Mesa Haulworks Garage web site for repairs,Parts, Accessories and Off Road

Need a wed site design for our light duty truck repair shop, also need to be able to sell our products from this page as well. Has our logo as the headliner and brief description of what we do and our history. An example of what we would want it to work like can be seen at www.garvinsfuelworks.example . This is a good example of style and accesses ability to buy parts we have.

Target Market(s)

Light duty Diesel truck owners(Brell,Kastor,Vantorine)

Industry/Entity Type

Shop

Number of Pages Required

3 page

Font styles to use
Other font styles liked:
• The same font as our logo

Requirements
Must have
• A little about the shop and all of our services,availability to purchase our products, also a map of where we are located.
Nice to have
• I like the design of www.Garvinsfuelworks.example. Its easy to use and very descriptive of parts available

```html
<!DOCTYPE html>
<html lang="en">
<head>
<meta charset="utf-8">
<title>Frequently Asked Questions – Lone Mesa Haulworks Garage</title>
<link href="https://fonts.googleapis.com/css2?family=Oswald:wght@400;500;700&family=Open+Sans:wght@400;600;700&display=swap" rel="stylesheet">
<style>
:root{
  --ink:#1d1d1f;
  --text:#3b3b3d;
  --muted:#77777a;
  --red:#c4161c;
  --nav:#1f1f21;
  --panel:#eeeeef;
  --rule:#d4d4d6;
  --footer:#e6e6e8;
  --white:#ffffff;
}
*{box-sizing:border-box;margin:0;padding:0}
html,body{width:891px;height:1200px;overflow:hidden;background:var(--white)}
body{font-family:"Open Sans",Arial,sans-serif;color:var(--text);position:relative}

.site-nav{position:absolute;top:0;left:0;width:891px;height:40px;background:var(--nav);display:flex;align-items:center;padding:0 54px;z-index:3}
.brand{display:flex;align-items:center;gap:8px;color:var(--white);font-family:"Oswald",sans-serif;font-weight:700;font-size:14px;letter-spacing:.5px;text-transform:uppercase}
.brand-mark{width:12px;height:12px;background:var(--red)}
.nav-links{display:flex;gap:30px;margin-left:auto;margin-right:140px;list-style:none}
.nav-links li{color:#cfcfd2;font-family:"Oswald",sans-serif;font-size:11px;letter-spacing:1px;text-transform:uppercase}

.hero{position:absolute;top:40px;left:0;width:891px;height:375px;overflow:hidden}
.hero-photo{position:absolute;inset:0;background:radial-gradient(ellipse at 20% 30%,#9b9b9e 0%,#6f6f72 35%,#3e3e41 70%,#2a2a2c 100%)}
.hero-veil{position:absolute;left:0;top:70px;width:891px;height:170px;background:rgba(255,255,255,.82)}
.hero-title{position:absolute;left:54px;top:84px;font-family:"Oswald",sans-serif;font-weight:700;font-size:60px;line-height:66px;color:var(--ink);letter-spacing:.5px}
.faq-tag{position:absolute;left:54px;bottom:0;width:128px;height:46px;background:var(--red);color:var(--white);font-family:"Oswald",sans-serif;font-weight:700;font-size:24px;display:flex;align-items:center;justify-content:center;letter-spacing:2px}

.faq{position:absolute;top:430px;left:54px;width:792px;display:flex;gap:30px}
.faq-col{flex:1}
.faq-item{border-bottom:1px solid var(--rule);padding:12px 0}
.question{display:flex;gap:10px;align-items:flex-start}
.q-mark,.a-mark{font-family:"Oswald",sans-serif;font-weight:700;font-size:24px;line-height:24px;color:var(--ink);flex:0 0 22px}
.q-text{flex:1;font-size:12px;line-height:17px;color:var(--text)}
.chev{flex:0 0 14px;margin-top:4px}
.answer{display:flex;gap:10px;background:var(--panel);margin-top:10px;padding:12px 12px 12px 0}
.a-mark{color:var(--red)}
.a-body{flex:1;font-size:10px;line-height:14.5px;color:var(--muted)}
.a-body p+p{margin-top:8px}
.a-body ul{list-style:none;margin:6px 0}
.a-body li::before{content:"– "}

.site-footer{position:absolute;left:0;top:1052px;width:891px;height:148px;background:var(--footer);padding:14px 54px 0}
.footer-top{display:flex;gap:40px;padding-bottom:8px;border-bottom:1px solid var(--rule)}
.footer-top h4,.footer-cols h4{font-family:"Oswald",sans-serif;font-size:11px;letter-spacing:1px;color:var(--ink);font-weight:500}
.signup{width:180px;height:18px;border:1px solid #bdbdc0;background:var(--white);margin-top:4px}
.footer-cols{display:flex;gap:90px;padding-top:10px}
.footer-cols ul{list-style:none;margin-top:4px;display:grid;grid-template-columns:auto auto;gap:2px 24px}
.footer-cols li{font-size:9px;color:var(--muted)}
.copyright{position:absolute;left:54px;bottom:8px;font-size:8px;color:var(--muted)}
</style>
</head>
<body>

<header class="site-nav">
  <div class="brand"><span class="brand-mark"></span>Lone Mesa Haulworks Garage</div>
  <ul class="nav-links"><li>Products</li><li>Services</li><li>About Us</li><li>FAQ</li></ul>
</header>

<section class="hero">
  <div class="hero-photo" role="img" aria-label="Close-up photograph of engine gears and timing belt in grey tones"></div>
  <div class="hero-veil"></div>
  <h1 class="hero-title">FREQUENTLY ASKED<br>QUESTIONS</h1>
  <div class="faq-tag">FAQ</div>
</section>

<main class="faq">
  <div class="faq-col">
    <div class="faq-item">
      <div class="question"><span class="q-mark">Q.</span><p class="q-text">Is tire pressure really that important? I mean, they pressure is a few pounds high or low, what does it really matter?</p><svg class="chev" width="14" height="14" viewBox="0 0 14 14"><path d="M3 5l4 4 4-4" fill="none" stroke="#1d1d1f" stroke-width="1.6"/></svg></div>
      <div class="answer"><span class="a-mark">A.</span><div class="a-body"><p>Tire pressure is extremely important to the performance and the SAFETY of your vehicle. You wouldn't think so, but you should check your pressure frequently, at least monthly. If your pressure is too high or too low, it hurts your gas mileage and wears the tread unevenly. Over time it can even affect braking and handling, and that puts your truck, your load and your family at risk on every trip. A quick check at the pump takes only a minute and keeps you rolling safely.</p></div></div>
    </div>
    <div class="faq-item">
      <div class="question"><span class="q-mark">Q.</span><p class="q-text">How often should I change my oil? I've heard different things. Can you tell me the best schedule?</p><svg class="chev" width="14" height="14" viewBox="0 0 14 14"><path d="M5 3l4 4-4 4" fill="none" stroke="#1d1d1f" stroke-width="1.6"/></svg></div>
    </div>
    <div class="faq-item">
      <div class="question"><span class="q-mark">Q.</span><p class="q-text">I'm always told about regular maintenance. Is the cost of service or the expense of car maintenance "pay off" in the long run?</p><svg class="chev" width="14" height="14" viewBox="0 0 14 14"><path d="M5 3l4 4-4 4" fill="none" stroke="#1d1d1f" stroke-width="1.6"/></svg></div>
    </div>
    <div class="faq-item">
      <div class="question"><span class="q-mark">Q.</span><p class="q-text">I got my oil changed every 3-4 months religiously! My "oil" light came on and when I checked, my car was almost 2 1/2 quarts low on oil! How can this be?</p><svg class="chev" width="14" height="14" viewBox="0 0 14 14"><path d="M5 3l4 4-4 4" fill="none" stroke="#1d1d1f" stroke-width="1.6"/></svg></div>
    </div>
  </div>

  <div class="faq-col">
    <div class="faq-item">
      <div class="question"><span class="q-mark">Q.</span><p class="q-text">I had my brakes serviced a while ago and they still squeal and squeak sometimes. Are my brakes safe?</p><svg class="chev" width="14" height="14" viewBox="0 0 14 14"><path d="M5 3l4 4-4 4" fill="none" stroke="#1d1d1f" stroke-width="1.6"/></svg></div>
    </div>
    <div class="faq-item">
      <div class="question"><span class="q-mark">Q.</span><p class="q-text">I want to maintain my car. What are the most common maintenance items recommended by vehicle manufacturers?</p><svg class="chev" width="14" height="14" viewBox="0 0 14 14"><path d="M3 5l4 4 4-4" fill="none" stroke="#1d1d1f" stroke-width="1.6"/></svg></div>
      <div class="answer"><span class="a-mark">A.</span><div class="a-body">
        <p>If you have your vehicle's owner's manual, it's the best place to start. If you don't have the manual, understand that every vehicle manufacturer will have slightly different recommended service intervals, but this is a list of the most common items:</p>
        <ul><li>Engine oil and filter change</li><li>Coolant or antifreeze flush and refill</li><li>Brake fluid service and pad inspection</li><li>Air and cabin filter replacement</li><li>Transmission fluid exchange</li><li>Spark plug replacement</li><li>Belts and hoses</li><li>Tire rotation</li></ul>
        <p>These are not listed in a particular order. It's important to understand that all inspections are recommended at regular intervals. Bring your truck by and we will help you build the right plan for your driving.</p>
      </div></div>
    </div>
    <div class="faq-item">
      <div class="question"><span class="q-mark">Q.</span><p class="q-text">Why is there a charge to diagnose my check engine light when national auto parts stores do it for free?</p><svg class="chev" width="14" height="14" viewBox="0 0 14 14"><path d="M5 3l4 4-4 4" fill="none" stroke="#1d1d1f" stroke-width="1.6"/></svg></div>
    </div>
    <div class="faq-item">
      <div class="question"><span class="q-mark">Q.</span><p class="q-text">I've got a new car. Will your service interfere with my manufacturer's new car warranty or do I have to return to the dealer?</p><svg class="chev" width="14" height="14" viewBox="0 0 14 14"><path d="M5 3l4 4-4 4" fill="none" stroke="#1d1d1f" stroke-width="1.6"/></svg></div>
    </div>
  </div>
</main>

<footer class="site-footer">
  <div class="footer-top">
    <div><h4>QUESTION</h4></div>
    <div><h4>NEWSLETTER</h4><div class="signup"></div></div>
  </div>
  <div class="footer-cols">
    <div><h4>PRODUCT</h4><ul><li>Engine</li><li>Filters</li><li>Lift Kits</li><li>Exhaust</li><li>Wheels</li><li>Lighting</li></ul></div>
    <div><h4>ABOUT US</h4><ul><li>History</li><li>Location</li><li>Services</li><li>Team</li></ul></div>
    <div><h4>CONNECT</h4><ul><li>Contact</li><li>Careers</li><li>Warranty</li><li>Reviews</li></ul></div>
  </div>
  <p class="copyright">© Lone Mesa Haulworks Garage. All rights reserved.</p>
</footer>

</body>
</html>
```